Interfaith organization needs a poster advertising event for youth

We need a poster advertising our annual Lantern Gathering and Summit, where youth of all different religions come together for dialogue, friendship, fun, art, and musical performances. The poster should be have a front advertising the event, and the back should have more detailed descriptions of the event and submissions. It should be fun and eye catching!

Target Market(s)

Youth and Religious Organizations

Industry/Entity Type

Festival

Font styles to use
Serif

Requirements
Must have
• Pictures, poster-feel, contact information, etc. Logos of Bright Harbor Allies and Crossroads Young Leaders Circle of Maple Valley

```html
<!DOCTYPE html>
<html lang="en">
<head>
<meta charset="utf-8">
<title>Lantern Gathering and Summit – Poster</title>
<link rel="stylesheet" href="https://fonts.googleapis.com/css2?family=Cinzel:wght@400;600;700&family=Crimson+Pro:wght@400;600;700&family=Roboto+Slab:wght@300;400&display=swap">
<style>
  :root {
    --ink: #111111;
    --title-green: #1f4a3c;
    --title-black: #121212;
    --gold: #e9b25a;
    --white: #ffffff;
    --band: #000000;
    --partner-blue: #2f64a8;
    --badge-blue: #1f63a8;
    --ring: #9a6a36;
    --sky-top: #4f9fa2;
    --sky-mid: #c9dfb8;
    --sky-glow: #f6dc8a;
    --sky-low: #d99a52;
  }
  * { margin: 0; padding: 0; box-sizing: border-box; }
  html, body { width: 835px; height: 1200px; overflow: hidden; background: var(--white); }
  .poster { position: relative; width: 835px; height: 1200px; overflow: hidden; background: var(--white); font-family: "Crimson Pro", Georgia, serif; }

  /* Header */
  .header {
    position: absolute; left: 0; top: 0; width: 835px; height: 337px;
    background:
      radial-gradient(ellipse 55% 50% at 20% 60%, rgba(255,244,180,0.95), rgba(255,244,180,0) 70%),
      radial-gradient(ellipse 40% 25% at 88% 88%, rgba(200,150,110,0.55), rgba(200,150,110,0) 70%),
      linear-gradient(180deg, var(--sky-top) 0%, #8fc3b3 22%, var(--sky-mid) 45%, var(--sky-glow) 70%, var(--sky-low) 100%);
  }
  .org-line {
    position: absolute; left: 0; right: 0; top: 26px; text-align: center;
    font-family: "Cinzel", Georgia, serif; font-size: 22px; color: var(--ink); letter-spacing: 0.5px;
  }
  .org-mark {
    position: absolute; left: 60px; top: 105px; width: 190px; height: 190px;
    display: flex; align-items: center; justify-content: center; text-align: center;
  }
  .org-mark svg { position: absolute; inset: 0; }
  .org-mark span {
    position: relative; width: 140px; font-family: "Cinzel", Georgia, serif; font-weight: 700;
    font-size: 17px; line-height: 1.25; color: var(--ring);
  }
  .edition {
    position: absolute; left: 300px; top: 76px;
    font-family: "Cinzel", Georgia, serif; font-weight: 400; font-size: 48px; color: var(--title-green); letter-spacing: 1px;
  }
  .edition sup { font-size: 26px; vertical-align: 18px; }
  .event-title {
    position: absolute; left: 300px; top: 140px;
    font-family: "Cinzel", Georgia, serif; font-weight: 400; font-size: 47px; line-height: 66px; color: var(--title-black);
  }
  .tagline {
    position: absolute; left: 40px; top: 296px; white-space: nowrap;
    font-family: "Cinzel", Georgia, serif; font-size: 20px; font-weight: 700; color: var(--ink); letter-spacing: 0.3px;
  }
  .tagline em { font-style: normal; font-weight: 400; color: var(--white); margin-left: 10px; }

  /* Photo areas */
  .photo { position: absolute; }
  .photo-dancer {
    left: 0; top: 339px; width: 275px; height: 300px;
    background:
      radial-gradient(ellipse 35% 20% at 55% 20%, rgba(200,60,40,0.7), rgba(200,60,40,0) 70%),
      radial-gradient(ellipse 30% 22% at 45% 48%, rgba(150,90,70,0.85), rgba(150,90,70,0) 70%),
      radial-gradient(ellipse 55% 35% at 50% 88%, rgba(240,200,40,0.95), rgba(240,200,40,0) 75%),
      radial-gradient(ellipse 25% 45% at 88% 75%, rgba(180,30,30,0.6), rgba(180,30,30,0) 70%),
      linear-gradient(160deg, #f1eee8, #d9d2c6 60%, #b9a890);
  }
  .photo-group {
    left: 282px; top: 339px; width: 553px; height: 300px;
    background:
      radial-gradient(ellipse 10% 12% at 18% 35%, rgba(220,170,140,0.9), rgba(220,170,140,0) 75%),
      radial-gradient(ellipse 10% 12% at 38% 30%, rgba(220,170,140,0.9), rgba(220,170,140,0) 75%),
      radial-gradient(ellipse 10% 12% at 63% 32%, rgba(220,170,140,0.9), rgba(220,170,140,0) 75%),
      radial-gradient(ellipse 10% 12% at 88% 33%, rgba(220,170,140,0.9), rgba(220,170,140,0) 75%),
      radial-gradient(ellipse 50% 22% at 50% 58%, rgba(200,150,120,0.55), rgba(200,150,120,0) 75%),
      linear-gradient(180deg, #ececea 0%, #e2e2de 35%, #2a2a2a 60%, #1c1c22 100%);
  }
  .photo-crowd {
    left: 0; top: 646px; width: 297px; height: 201px;
    background:
      radial-gradient(ellipse 30% 35% at 25% 70%, rgba(110,100,90,0.8), rgba(110,100,90,0) 70%),
      radial-gradient(ellipse 25% 35% at 65% 65%, rgba(130,100,80,0.8), rgba(130,100,80,0) 70%),
      radial-gradient(ellipse 25% 30% at 88% 60%, rgba(110,50,60,0.7), rgba(110,50,60,0) 70%),
      linear-gradient(180deg, #e8e4de 0%, #cfc6bc 35%, #7a6a62 100%);
  }
  .photo-drummer {
    left: 304px; top: 646px; width: 152px; height: 201px;
    background:
      radial-gradient(ellipse 35% 30% at 45% 45%, rgba(120,80,50,0.9), rgba(120,80,50,0) 75%),
      radial-gradient(ellipse 70% 25% at 50% 92%, rgba(140,40,25,0.95), rgba(140,40,25,0) 80%),
      linear-gradient(180deg, #f4ecea 0%, #f0dcdc 50%, #b07050 100%);
  }
  .photo-tables {
    left: 463px; top: 646px; width: 372px; height: 201px;
    background:
      radial-gradient(ellipse 30% 20% at 35% 85%, rgba(110,70,160,0.85), rgba(110,70,160,0) 75%),
      radial-gradient(ellipse 20% 30% at 28% 55%, rgba(150,40,50,0.7), rgba(150,40,50,0) 70%),
      radial-gradient(ellipse 18% 35% at 85% 65%, rgba(60,60,70,0.8), rgba(60,60,70,0) 70%),
      radial-gradient(ellipse 20% 20% at 60% 20%, rgba(230,180,80,0.6), rgba(230,180,80,0) 70%),
      linear-gradient(180deg, #ece4da 0%, #d8ccc0 40%, #8a7a86 100%);
  }

  /* Info band */
  .info-band { position: absolute; left: 0; top: 854px; width: 835px; height: 346px; background: var(--band); }
  .forum-title {
    position: absolute; left: 0; right: 0; top: 18px; text-align: center;
    font-family: "Roboto Slab", Georgia, serif; font-weight: 300; font-size: 33px; line-height: 46px; color: var(--gold);
  }
  .date-line {
    position: absolute; left: 0; right: 0; top: 116px; text-align: center;
    font-family: "Crimson Pro", Georgia, serif; font-weight: 700; font-size: 29px; line-height: 34px; color: var(--white);
  }
  .date-line sup { font-size: 16px; }
  .date-line .divider { font-weight: 400; margin: 0 4px; }
  .date-line .time { font-weight: 400; }
  .venue {
    position: absolute; left: 0; right: 0; top: 154px; text-align: center;
    font-family: "Crimson Pro", Georgia, serif; font-size: 25px; color: var(--white);
  }

  .partners { position: absolute; left: 32px; top: 234px; display: flex; align-items: center; gap: 22px; }
  .partner-name {
    display: flex; align-items: center; gap: 10px;
    font-family: "Crimson Pro", Georgia, serif; font-size: 31px; line-height: 27px; color: var(--partner-blue);
  }
  .partner-name i { flex: none; width: 44px; height: 44px; border-radius: 50%; border: 2px solid var(--white); align-self: flex-start; }
  .partner-badge { width: 86px; height: 78px; background: var(--badge-blue); }

  .contacts { position: absolute; left: 367px; top: 212px; list-style: none; }
  .contacts li {
    display: flex; align-items: center; gap: 12px; height: 28px;
    font-family: "Roboto Slab", Georgia, serif; font-weight: 300; font-size: 16px; color: var(--white);
  }
  .contacts svg { flex: none; width: 14px; height: 14px; }
</style>
</head>
<body>
<main class="poster">
  <header class="header">
    <p class="org-line">Crossroads Young Leaders Circle of Maple Valley's</p>
    <div class="org-mark">
      <svg viewBox="0 0 190 190" aria-hidden="true"><circle cx="95" cy="95" r="92" fill="none" stroke="var(--ring)" stroke-width="3"/></svg>
      <span>Crossroads Young Leaders Circle of Maple Valley</span>
    </div>
    <h2 class="edition">13<sup>TH</sup> Annual</h2>
    <h1 class="event-title">Lantern Gathering<br>&amp; Summit</h1>
    <p class="tagline">Teens expressing their faith through<em>Art, Music, and Dialogue</em></p>
  </header>

  <div class="photo photo-dancer" role="img" aria-label="Photo of a smiling young dancer in a red and gold costume"></div>
  <div class="photo photo-group" role="img" aria-label="Photo of four teens sitting together making heart shapes with their hands"></div>
  <div class="photo photo-crowd" role="img" aria-label="Photo of teens mingling and talking in a community hall"></div>
  <div class="photo photo-drummer" role="img" aria-label="Photo of a teen performing on traditional drums"></div>
  <div class="photo photo-tables" role="img" aria-label="Photo of teens in dialogue around tables with purple cloths"></div>

  <section class="info-band">
    <h2 class="forum-title">INTERFAITH YOUTH FORUM<br>THIS YEAR'S THEME "Is Religion Cool?"</h2>
    <p class="date-line">Sunday March 19<sup>th</sup>, 2017 <span class="divider">|</span> <span class="time">11:00am - 5:00pm</span></p>
    <p class="venue">Cedar Hall Community Center</p>

    <div class="partners">
      <div class="partner-name"><span>Bright<br>Harbor<br>Allies</span><i></i></div>
      <div class="partner-badge" role="img" aria-label="Partner badge"></div>
    </div>

    <ul class="contacts">
      <li><svg viewBox="0 0 14 14" aria-hidden="true"><rect x="1" y="3" width="12" height="8" fill="var(--white)"/><path d="M1 3 L7 8 L13 3" fill="none" stroke="var(--band)" stroke-width="1.2"/></svg>hello@crossroadscircle.org</li>
      <li><svg viewBox="0 0 14 14" aria-hidden="true"><circle cx="7" cy="7" r="5.5" fill="none" stroke="var(--white)" stroke-width="1.3"/><ellipse cx="7" cy="7" rx="2.5" ry="5.5" fill="none" stroke="var(--white)" stroke-width="1"/><line x1="1.5" y1="7" x2="12.5" y2="7" stroke="var(--white)" stroke-width="1"/></svg>www.crossroadscircle.org</li>
      <li><svg viewBox="0 0 14 14" aria-hidden="true"><circle cx="7" cy="7" r="6" fill="var(--white)"/></svg>Crossroads Young Leaders Circle of Maple Valley</li>
      <li><svg viewBox="0 0 14 14" aria-hidden="true"><path d="M7 1 C4 1 2.5 3.2 2.5 5.4 C2.5 8.5 7 13 7 13 C7 13 11.5 8.5 11.5 5.4 C11.5 3.2 10 1 7 1 Z" fill="var(--white)"/><circle cx="7" cy="5.4" r="1.6" fill="var(--band)"/></svg>4410 Linden Grove Ave, Maple Valley, CA 90000</li>
    </ul>
  </section>
</main>
</body>
</html>
```